Landscaping | Turf | With Future Opportunities

The Meadow Lawn (themeadowlawn-example.com) is looking for a website rebuild.
Please see the brief attached.

The Meadow Lawn is the #1 artificial grass instillation company in southern california. They are small, but do great work.

This is a project where you are able to utilize your creative-genius! Imply integrations for Yelp reviews, add charts that are lighter grey for the competition, take images from our site and Yelp if you're going for a more real-approach.

We are open to creativity!! Competitor sites are not very appealing. We want users to be able to come to our site and have all the information to make an educated decision but also see that we value our online presence.

We are using wordpress so the designer would need to be able to code this into our site upon completion.
Updates

Target Market(s)

Homeowners, 25+ years old, southern california

Industry/Entity Type

Landscaping

Coding

Coded - Design and coding required

Number of Pages Required

3 page

Colors
9bcb3b

Requirements
Must have
• Pages must be responsive (desktop and mobile).
• Must be able to input into wordpress.
• Please use your best judgement to create the following:
• - Form fill so Todd can reach out for estimate times: info needed are first and last name, email, phone number, address and an optional box for memo that lead to his inbox
• - Why we are different (see brief)
• - A link to his Yelp page will reviews/ testimonials
• - Photos for his work in his three products: Front yard, backyard, putting greens
• - Certification, reliability, contact info
• - A clear CTA to leave their info with inquiries
• How many pages would this entail? We don't want a ton of unnecessary stuff on site, we dont want it to look cluttered, but we don't want it to be missing info.
• **Please do not rely on the designated pages. Use your best judgement.
• Use current site for color.
Should not have
• Many competitor sites look dated.
• The text and images must be crawl-able on Google so make sure the site reflects this (psd files, not pdf or jpegs)

```html
<!DOCTYPE html>
<html lang="en">
<head>
<meta charset="utf-8">
<title>The Meadow Lawn — Artificial Grass Installation</title>
<link href="https://fonts.googleapis.com/css2?family=Poppins:wght@300;400;500;600;700&display=swap" rel="stylesheet">
<style>
:root{
  --lime:#8dc63f;
  --lime-bright:#9bcb3b;
  --orange:#f7a900;
  --coral:#f0595a;
  --forest:#386b1d;
  --forest-deep:#2c5716;
  --beige:#f8f5ec;
  --ink:#2b2b2b;
  --muted:#6d6d6d;
  --row-grey:#ececec;
  --white:#ffffff;
}
*{box-sizing:border-box;margin:0;padding:0}
html,body{width:1200px;height:3446px;overflow:hidden}
body{font-family:"Poppins",sans-serif;color:var(--ink);background:var(--white);position:relative}
.abs{position:absolute}

/* top bar */
.topbar{top:0;left:0;width:1200px;height:44px;background:var(--orange);color:var(--white);font-size:11px}
.topbar .contact{left:108px;top:14px;display:flex;gap:12px;align-items:center}
.topbar .contact span{display:flex;align-items:center;gap:6px}
.topbar .sep{width:1px;height:12px;background:rgba(255,255,255,.7)}
.topbar .social{right:120px;top:15px;display:flex;gap:12px}
.topbar .social i{display:block;width:12px;height:12px;border-radius:50%;background:var(--white)}

/* header */
.header{top:44px;left:0;width:1200px;height:96px;background:var(--white)}
.brand{left:103px;top:34px;display:flex;align-items:center;gap:10px;font-weight:700;font-size:22px;color:var(--forest-deep);letter-spacing:.5px}
.brand .mark{width:16px;height:16px;background:var(--forest-deep)}
.nav{left:594px;top:36px;display:flex;align-items:center;font-size:13px;font-weight:500}
.nav a{color:var(--ink);text-decoration:none;margin-right:60px}
.nav a.active{color:var(--lime)}
.btn{display:inline-flex;align-items:center;justify-content:center;border-radius:20px;font-family:inherit;text-decoration:none}
.nav .btn{background:var(--lime);color:var(--white);height:30px;padding:0 18px;font-size:12px;margin-left:-2px}

/* hero */
.hero{top:140px;left:0;width:1200px;height:405px;background:linear-gradient(180deg,#4a6b3a 0%,#3f8a22 22%,#48a425 55%,#3f9520 100%);color:var(--white);text-align:center}
.hero h1{position:absolute;top:140px;width:100%;font-size:37px;font-weight:600}
.hero .lead{position:absolute;top:188px;width:100%;font-size:19px;font-weight:400}
.hero .cta{position:absolute;top:254px;left:356px;display:flex;align-items:center;gap:18px}
.hero .cta .btn{height:34px;width:216px;background:#2f5c14;border:2px solid var(--lime);color:var(--white);font-size:11px;letter-spacing:1px}
.hero .cta .call{font-size:15px;font-weight:600}
.hero .cta .num{font-size:28px;font-weight:600;color:#b6ee3c;margin-left:8px}
.hero .arrow{position:absolute;top:182px;width:38px;height:38px;border-radius:50%;background:var(--white);display:flex;align-items:center;justify-content:center}

/* intro / services */
.intro{top:545px;left:0;width:1200px;height:699px;background:var(--beige)}
.intro h2{position:absolute;top:30px;width:100%;text-align:center;color:var(--lime);font-size:28px;font-weight:600;line-height:34px}
.card{top:147px;width:207px;height:366px;background:var(--white);border-radius:12px;box-shadow:0 2px 8px rgba(0,0,0,.06)}
.card .photo{height:241px;border-radius:12px 12px 0 0}
.card .label{position:absolute;top:312px;width:100%;text-align:center;color:var(--lime);font-size:13px;font-weight:500}
.to-top{left:1106px;top:462px;width:28px;height:28px;background:#c8c8c8;display:flex;align-items:center;justify-content:center}
.services{top:568px;left:124px;width:980px;font-size:11px}
.services .intro-col{position:absolute;left:0;top:0}
.services .intro-col b{font-weight:500;display:block}
.services .intro-col a{color:var(--forest);text-decoration:underline;display:block;margin-top:8px}
.services ul{position:absolute;list-style:none;top:0}
.services li{margin-bottom:12px;display:flex;align-items:center;gap:8px;color:#444}
.services li:before{content:"";width:5px;height:5px;border-radius:50%;background:var(--lime)}

/* difference */
.different{top:1244px;left:0;width:1200px;height:726px;background:linear-gradient(160deg,#3d5a35 0%,#5b7f4a 40%,#3b6a2a 70%,#2f4f24 100%);text-align:center;color:var(--white)}
.different h2{position:absolute;top:34px;width:100%;font-size:28px;font-weight:600;color:var(--lime-bright);letter-spacing:1px}
.different .sub{position:absolute;top:70px;width:100%;font-size:16px}
.table{left:122px;top:174px;width:889px;height:481px;background:var(--white);border-radius:10px;overflow:hidden}
.thead{position:absolute;top:0;height:67px;display:flex;align-items:center;justify-content:center;font-size:13px;font-weight:500;color:var(--white)}
.row{position:absolute;left:0;width:889px;display:flex}
.row.alt{background:var(--row-grey)}
.row .feat{width:301px;padding:8px 12px 0 12px;text-align:left}
.row .feat b{display:block;font-size:12px;font-weight:600;color:var(--ink)}
.row .feat span{display:block;font-size:10.5px;color:var(--muted);line-height:13px}
.row .them{position:absolute;left:611px;width:278px;top:0;bottom:0;display:flex;align-items:center;justify-content:center;font-size:11px;color:#444}
.us-col{left:423px;top:140px;width:310px;height:538px;background:var(--white);border-radius:10px;box-shadow:0 4px 16px rgba(0,0,0,.25);overflow:hidden}
.us-col .head{height:101px;background:var(--lime);display:flex;align-items:center;justify-content:center;font-size:13px;font-weight:500;color:var(--white);padding-top:20px}
.us-cell{position:absolute;left:0;width:310px;display:flex;align-items:center;justify-content:center;text-align:center;font-size:11px;color:#444;padding:0 34px;line-height:14px}
.us-cell.alt{background:var(--row-grey)}

/* clients */
.clients{top:2000px;left:103px;width:966px;height:432px;background:var(--white);border:1px solid #e6e6e6}
.clients .photo{position:absolute;left:0;top:0;width:380px;height:432px;background:linear-gradient(160deg,#d46a4e 0%,#6aa33a 30%,#4f9a2a 60%,#3e8722 100%)}
.clients .photo h3{position:absolute;left:110px;bottom:20px;color:var(--white);font-size:26px;font-weight:500}
.clients .quote{position:absolute;left:380px;top:0;width:586px;height:432px;text-align:center}
.clients blockquote{position:absolute;top:160px;left:60px;width:466px;font-size:15px;line-height:22px;color:#333}
.clients .rating{position:absolute;top:225px;width:100%;font-size:13px;color:#333}
.clients .rating small{font-size:9px;color:var(--muted);letter-spacing:1px}
.dots{position:absolute;top:270px;left:0;width:100%;display:flex;justify-content:center;gap:6px}
.dots i{width:10px;height:10px;border-radius:50%;border:1px solid #bbb}
.dots i.on{background:var(--forest);border-color:var(--forest)}

/* faq + quote */
.lead-band{top:2490px;left:0;width:1200px;height:591px;background:var(--forest)}
.faq{left:103px;top:0;width:463px;height:591px;background:#f1f1f1}
.faq h3{position:absolute;top:22px;width:100%;text-align:center;font-size:22px;font-weight:500}
.faq-item{position:absolute;left:8px;width:447px;height:38px;background:var(--orange);border-radius:4px;color:var(--white);font-size:11px;font-weight:600;display:flex;align-items:center;justify-content:space-between;padding:0 12px 0 20px}
.faq-answer{position:absolute;left:8px;top:100px;width:447px;height:110px;background:var(--white);font-size:12px;line-height:19px;color:#444;padding:12px 20px}
.quote-form{left:630px;top:0;width:423px;color:var(--white)}
.quote-form h3{position:absolute;top:50px;font-size:26px;font-weight:600;color:var(--lime-bright)}
.quote-form .sub{position:absolute;top:90px;font-size:15px;width:423px}
.field{position:absolute;height:34px;background:var(--white);border-radius:17px;color:#888;font-size:11px;display:flex;align-items:center;padding:0 16px}
.field.area{align-items:flex-start;padding-top:16px;border-radius:14px}
.quote-form .btn{position:absolute;top:501px;left:0;width:175px;height:35px;background:var(--lime);color:var(--white);font-size:11px}

/* footer */
.footer{top:3081px;left:0;width:1200px;height:365px;background:var(--beige);text-align:center}
.footer .brand{position:absolute;left:0;width:100%;top:44px;justify-content:center}
.footer .btn{position:absolute;top:99px;left:457px;width:221px;height:42px;background:var(--lime);color:var(--white);font-size:12px;letter-spacing:1px}
.footer .info{position:absolute;top:158px;width:100%;font-size:12px;line-height:23px;color:#333}
.footer .info b{font-weight:600}
.footer .social{position:absolute;top:273px;left:0;width:100%;display:flex;justify-content:center;gap:24px}
.footer .social i{width:13px;height:13px;border-radius:50%;background:var(--lime)}
.footer .copy{position:absolute;top:307px;width:100%;font-size:10px;color:var(--muted)}
</style>
</head>
<body>

<!-- top bar -->
<div class="topbar abs">
  <div class="contact abs">
    <span><svg width="11" height="11" viewBox="0 0 24 24"><path fill="#fff" d="M6.6 10.8a15.1 15.1 0 0 0 6.6 6.6l2.2-2.2c.3-.3.7-.4 1-.2 1.1.4 2.3.6 3.6.6.6 0 1 .4 1 1V20c0 .6-.4 1-1 1A17 17 0 0 1 3 4c0-.6.4-1 1-1h3.5c.6 0 1 .4 1 1 0 1.3.2 2.5.6 3.6.1.3 0 .7-.2 1z"/></svg>555.014.2290</span>
    <i class="sep"></i>
    <span><svg width="12" height="10" viewBox="0 0 24 18"><path fill="#fff" d="M2 0h20a2 2 0 0 1 2 2v14a2 2 0 0 1-2 2H2a2 2 0 0 1-2-2V2a2 2 0 0 1 2-2zm10 8 10-6H2z"/></svg>office@example.com</span>
  </div>
  <div class="social abs"><i></i><i></i><i></i></div>
</div>

<!-- header -->
<header class="header abs">
  <div class="brand abs"><span class="mark"></span>THE MEADOW LAWN</div>
  <nav class="nav abs">
    <a href="#" class="active">Home</a>
    <a href="#">Services</a>
    <a href="#">Reviews</a>
    <a href="#" class="btn">I want a FREE quote!</a>
  </nav>
</header>

<!-- hero -->
<section class="hero abs" role="img" aria-label="Photo of a freshly installed artificial turf lawn beside a hedge">
  <h1>Seamless Artificial Synthetic Turf</h1>
  <p class="lead">We pride ourselves as some of the best in California.</p>
  <div class="cta">
    <a href="#" class="btn">I WANT AN ESTIMATE</a>
    <span class="call">or Call Today<span class="num">555.014.2290</span></span>
  </div>
  <span class="arrow" style="left:73px"><svg width="14" height="14" viewBox="0 0 24 24"><path d="M15 5 8 12l7 7" fill="none" stroke="#8dc63f" stroke-width="3"/></svg></span>
  <span class="arrow" style="left:1022px"><svg width="14" height="14" viewBox="0 0 24 24"><path d="m9 5 7 7-7 7" fill="none" stroke="#8dc63f" stroke-width="3"/></svg></span>
</section>

<!-- intro & services -->
<section class="intro abs">
  <h2>We are a Southern California-Based, Professional,<br>Artificial Grass Installer</h2>
  <div class="card abs" style="left:103px"><div class="photo" role="img" aria-label="Front yard turf installation" style="background:linear-gradient(180deg,#7a8f6c,#3f8a23)"></div><div class="label">Frontyard</div></div>
  <div class="card abs" style="left:343px"><div class="photo" role="img" aria-label="Backyard turf installation" style="background:linear-gradient(180deg,#5d7a52,#4d9a2c)"></div><div class="label">Backyard</div></div>
  <div class="card abs" style="left:584px"><div class="photo" role="img" aria-label="Putting green with hedge" style="background:linear-gradient(180deg,#2f5a1e,#3c7d20 50%,#55a32c)"></div><div class="label">Putting Green</div></div>
  <div class="card abs" style="left:823px"><div class="photo" role="img" aria-label="Putting green flag on turf" style="background:linear-gradient(180deg,#6aa64a,#5a9c3e)"></div><div class="label" style="top:305px">Maintenance</div></div>
  <div class="to-top abs"><svg width="10" height="10" viewBox="0 0 24 24"><path d="m5 15 7-7 7 7" fill="none" stroke="#fff" stroke-width="3"/></svg></div>
  <div class="services abs">
    <div class="intro-col"><b>We handle everything for you!</b><a href="#">View all services</a></div>
    <ul style="left:267px"><li>Full Project Management</li><li>Design and 3D Modeling</li></ul>
    <ul style="left:510px"><li>Construction</li><li>Permits and Inspections</li></ul>
    <ul style="left:740px"><li>Irrigation and Drainage</li><li>Planting and Removal</li></ul>
  </div>
</section>

<!-- how are we different -->
<section class="different abs" role="group" aria-label="Comparison on a backdrop photo of turf and stone pavers">
  <h2>HOW ARE WE DIFFERENT?</h2>
  <p class="sub">We go above and beyond.</p>
  <div class="table abs">
    <div class="thead" style="left:0;width:301px;background:var(--coral)">Features &amp; Why They Are Important</div>
    <div class="thead" style="left:611px;width:278px;background:var(--orange)">What They Do</div>
    <div class="row alt" style="top:67px;height:62px"><div class="feat"><b>Estimates</b><span>Our first impression matters.</span></div><div class="them"><svg width="16" height="16" viewBox="0 0 24 24"><circle cx="12" cy="12" r="10" fill="none" stroke="#e53935" stroke-width="2"/><path d="m8 8 8 8m0-8-8 8" stroke="#e53935" stroke-width="2"/></svg></div></div>
    <div class="row" style="top:129px;height:60px"><div class="feat"><b>Timing</b><span>I know you're busy; I value your time.</span></div><div class="them"><svg width="16" height="16" viewBox="0 0 24 24"><circle cx="12" cy="12" r="10" fill="none" stroke="#e53935" stroke-width="2"/><path d="m8 8 8 8m0-8-8 8" stroke="#e53935" stroke-width="2"/></svg></div></div>
    <div class="row alt" style="top:189px;height:64px"><div class="feat"><b>Excavate</b><span>Digging deeper removes roots from the ground to improve stability, long term.</span></div><div class="them">2–3 inches</div></div>
    <div class="row" style="top:253px;height:78px"><div class="feat"><b>Nail</b><span>Artificial grass can lift over time; I ensure a tight fit with more nails, closer together for extra security.</span></div><div class="them">Every 5 inches</div></div>
    <div class="row alt" style="top:331px;height:69px"><div class="feat"><b>Seams</b><span>A big seam between two pieces of grass is not something to be proud of.</span></div><div class="them">Use nails every few inches</div></div>
    <div class="row" style="top:400px;height:81px"><div class="feat"><b>Personality</b><span>I run a local business; we are neighbors.</span></div><div class="them"><svg width="16" height="16" viewBox="0 0 24 24"><circle cx="12" cy="12" r="10" fill="none" stroke="#e53935" stroke-width="2"/><path d="m8 8 8 8m0-8-8 8" stroke="#e53935" stroke-width="2"/></svg></div></div>
  </div>
  <div class="us-col abs">
    <div class="head">What We Do</div>
    <div class="us-cell alt" style="top:101px;height:62px">Bring a piece of turf for you to touch and feel</div>
    <div class="us-cell" style="top:163px;height:60px">Punctual while detail-oriented</div>
    <div class="us-cell alt" style="top:223px;height:64px">4 inches</div>
    <div class="us-cell" style="top:287px;height:78px">Every 2 inches</div>
    <div class="us-cell alt" style="top:365px;height:69px">We glue all seams to join pieces together to make grass one, seamless roll</div>
    <div class="us-cell" style="top:434px;height:81px">We are considerate, friendly, and detail-oriented</div>
  </div>
</section>

<!-- clients -->
<section class="clients abs">
  <div class="photo" role="img" aria-label="Backyard putting green with flag beside a brick path"><h3>Our Clients</h3></div>
  <div class="quote">
    <svg class="abs" style="left:250px;top:62px" width="44" height="44" viewBox="0 0 44 44" fill="none" stroke="#3b8a2a" stroke-width="2"><rect x="12" y="4" width="26" height="18" rx="2"/><path d="M18 10h14M18 15h10"/><circle cx="12" cy="28" r="5"/><path d="M3 42c0-6 4-9 9-9s9 3 9 9"/><path d="m22 22 4 6"/></svg>
    <blockquote>“We are new customers of this company and have been very favorably impressed with the quality of the work performed by your employees.”</blockquote>
    <p class="rating">★★★★★ &nbsp;— <small>DANIEL K.</small></p>
    <div class="dots"><i class="on"></i><i></i><i></i><i></i><i></i></div>
  </div>
</section>

<!-- faq & quote form -->
<section class="lead-band abs">
  <div class="faq abs">
    <h3>Frequently Asked Questions</h3>
    <div class="faq-item" style="top:62px">This is a first question about turf?<svg width="16" height="16" viewBox="0 0 24 24"><circle cx="12" cy="12" r="11" fill="#fff"/><path d="M7 12h9m-4-4 4 4-4 4" fill="none" stroke="#f7a900" stroke-width="2.4"/></svg></div>
    <div class="faq-answer">We work with a select group of landscape contractors, water feature and lighting design specialists to ensure the garden design process, from initial concept to project completion, is smooth and seamless. This is a dummy text holder.</div>
    <div class="faq-item" style="top:222px">This is a first question about turf?<svg width="16" height="16" viewBox="0 0 24 24"><circle cx="12" cy="12" r="11" fill="#fff"/><path d="M7 12h9m-4-4 4 4-4 4" fill="none" stroke="#f7a900" stroke-width="2.4"/></svg></div>
    <div class="faq-item" style="top:274px">This is a first question about turf?<svg width="16" height="16" viewBox="0 0 24 24"><circle cx="12" cy="12" r="11" fill="#fff"/><path d="M7 12h9m-4-4 4 4-4 4" fill="none" stroke="#f7a900" stroke-width="2.4"/></svg></div>
    <div class="faq-item" style="top:326px">This is a first question about turf?<svg width="16" height="16" viewBox="0 0 24 24"><circle cx="12" cy="12" r="11" fill="#fff"/><path d="M7 12h9m-4-4 4 4-4 4" fill="none" stroke="#f7a900" stroke-width="2.4"/></svg></div>
    <div class="faq-item" style="top:378px">This is a first question about turf?<svg width="16" height="16" viewBox="0 0 24 24"><circle cx="12" cy="12" r="11" fill="#fff"/><path d="M7 12h9m-4-4 4 4-4 4" fill="none" stroke="#f7a900" stroke-width="2.4"/></svg></div>
    <div class="faq-item" style="top:430px">This is a first question about turf?<svg width="16" height="16" viewBox="0 0 24 24"><circle cx="12" cy="12" r="11" fill="#fff"/><path d="M7 12h9m-4-4 4 4-4 4" fill="none" stroke="#f7a900" stroke-width="2.4"/></svg></div>
    <div class="faq-item" style="top:482px">This is a first question about turf?<svg width="16" height="16" viewBox="0 0 24 24"><circle cx="12" cy="12" r="11" fill="#fff"/><path d="M7 12h9m-4-4 4 4-4 4" fill="none" stroke="#f7a900" stroke-width="2.4"/></svg></div>
    <div class="faq-item" style="top:534px">This is a first question about turf?<svg width="16" height="16" viewBox="0 0 24 24"><circle cx="12" cy="12" r="11" fill="#fff"/><path d="M7 12h9m-4-4 4 4-4 4" fill="none" stroke="#f7a900" stroke-width="2.4"/></svg></div>
  </div>
  <div class="quote-form abs">
    <h3>Get Your FREE Quote</h3>
    <p class="sub">Please fill up the form to get your quote</p>
    <div class="field" style="top:165px;left:0;width:202px">Name</div>
    <div class="field" style="top:165px;left:214px;width:207px">Email</div>
    <div class="field" style="top:216px;left:0;width:202px">Address</div>
    <div class="field" style="top:216px;left:214px;width:207px">Phone</div>
    <div class="field" style="top:273px;left:0;width:421px;justify-content:space-between;color:#444">Full Project Management<svg width="10" height="6" viewBox="0 0 10 6"><path d="M0 0h10L5 6z" fill="#333"/></svg></div>
    <div class="field area" style="top:326px;left:0;width:421px;height:145px">Describe briefly</div>
    <a href="#" class="btn">Get FREE Quote</a>
  </div>
</section>

<!-- footer -->
<footer class="footer abs">
  <div class="brand"><span class="mark"></span>THE MEADOW LAWN</div>
  <a href="#" class="btn">I WANT AN ESTIMATE</a>
  <p class="info"><b>Hi, I'm Todd</b> and I am available for you!<br><b>Call (555) 014 2290</b> or email me<br>at <b>info@themeadowlawn-example.com</b><br>Please reach out for a free, no obligation estimate.</p>
  <div class="social"><i></i><i></i><i></i></div>
  <p class="copy">© 2018 All Rights Reserved. The Meadow Lawn.</p>
</footer>

</body>
</html>
```